Private Medical Clinic needs a letterhead design

Letterhead that can be edited. Letter head is needed for printing official doctor's notes, referrals, etc in a medical clinic. The letterhead should use the attached logos

```html
<!DOCTYPE html>
<html lang="en">
<head>
<meta charset="utf-8">
<title>Quiet Meadow Family Medicine — Letterhead</title>
<link rel="stylesheet" href="https://fonts.googleapis.com/css2?family=Crimson+Text:wght@400;600&display=swap">
<style>
  :root {
    --backdrop: #e8e8e8;
    --paper: #ffffff;
    --band: #545849;
    --band-text: #e6e6df;
    --logo-text: #ffffff;
    --motif-band: rgba(200, 204, 188, 0.28);
    --motif-page: rgba(214, 217, 214, 0.55);
  }
  * { margin: 0; padding: 0; box-sizing: border-box; }
  html, body {
    width: 1200px;
    height: 800px;
    overflow: hidden;
    background: var(--backdrop);
    font-family: "Crimson Text", Georgia, serif;
  }
  .letterhead {
    position: absolute;
    left: 331px;
    top: 20px;
    width: 537px;
    height: 760px;
    background: var(--paper);
    overflow: hidden;
  }
  .header-band {
    position: absolute;
    inset: 0 0 auto 0;
    height: 143px;
    background: var(--band);
  }
  .header-motif {
    position: absolute;
    left: 0;
    top: 4px;
    width: 110px;
    height: 139px;
    background: radial-gradient(circle at 45% 32%, var(--motif-band) 0%, rgba(200,204,188,0.12) 38%, transparent 62%);
  }
  .contact {
    position: absolute;
    left: 38px;
    top: 72px;
    color: var(--band-text);
    font-size: 8px;
    line-height: 11.5px;
    letter-spacing: 0.1px;
  }
  .contact .label {
    font-size: 6px;
    letter-spacing: 0.4px;
    text-transform: uppercase;
    margin-right: 2px;
  }
  .contact .gap { display: inline-block; width: 7px; }
  .contact .domain { font-weight: 600; letter-spacing: 0.6px; }
  .brand {
    position: absolute;
    right: 38px;
    top: 60px;
    display: flex;
    align-items: flex-start;
    gap: 6px;
    color: var(--logo-text);
  }
  .brand-mark {
    width: 11px;
    height: 11px;
    border-radius: 50%;
    background: var(--logo-text);
    margin-top: 4px;
  }
  .brand-text { display: flex; flex-direction: column; }
  .brand-name {
    font-size: 30px;
    line-height: 30px;
    font-weight: 400;
    letter-spacing: -0.3px;
  }
  .brand-tagline {
    font-size: 7.5px;
    letter-spacing: 1.6px;
    text-transform: uppercase;
    margin-top: 5px;
    margin-left: 2px;
  }
  .page-motif {
    position: absolute;
    left: 276px;
    top: 380px;
    width: 261px;
    height: 380px;
    background:
      radial-gradient(circle at 44% 32%, var(--motif-page) 0%, rgba(214,217,214,0.3) 28%, transparent 46%),
      radial-gradient(circle at 74% 58%, rgba(214,217,214,0.4) 0%, rgba(214,217,214,0.2) 20%, transparent 34%);
  }
</style>
</head>
<body>
  <main class="letterhead">
    <header class="header-band">
      <div class="header-motif" role="img" aria-label="Faint dandelion seed head illustration"></div>
      <address class="contact">
        <span class="label">Phone</span> 555.014.2280<span class="gap"></span><span class="label">Mail</span> hello@quietmeadow.com<br>
        470 Linden Row, Suite 12B, Alderbrook, FL 30418<br>
        www.<span class="domain">QUIETMEADOW</span>.com
      </address>
      <div class="brand">
        <span class="brand-mark"></span>
        <div class="brand-text">
          <span class="brand-name">Quiet Meadow</span>
          <span class="brand-tagline">Family Medicine</span>
        </div>
      </div>
    </header>
    <div class="page-motif" role="img" aria-label="Faint watermark illustration of two dandelions releasing seeds"></div>
  </main>
</body>
</html>
```